CedarBight.Lawyer, a new website for Morris.

Looking for a professional web site for my small country law firm.
I have a logo, chart, map, my photo, office photo, google analytics code, my drone video on YouTube, "Brantwell Beacon Skyrun, also on www.loftcove.guide", and text content. I am figuring out how to get those into digital forms.
First page needs a professional look. Here's where I am really hoping for your skill set.
Banner should be well designed so as to "ease" the viewer into confidence in my firm
Prefer the "white backround", less cluttered style of design.
My office has been in Key Center, main and only town of Key Peninsula, for 25 years, with emphasis on real property matters. Naturally land lasts longer than people, so estates, trusts and succession issues are relevant.
Local KP is the heart of southern Puget Sound, 75 miles of spectacular residential waterfront. We have the best land, waterfront, beaches and views in Puget Sound, however of course Seattle and the San Juan Islands could not be disregarded. It's that we have the most privacy, the best old growth Doug Firs, wildlife and low population density.
Puget Sound conditions are very specific for residential development.
One must consider:
Topography, hydro-geology, geomorphology, hill slope stability, soils must support septic systems, individual wells, prescriptive, express and implied easement issues, boundary lines don't always line up with surveys or expectations, or historic use, thus adverse possession abounds environmentally protected shorelines and wetlands, all challenges, but ohh.., the views and unique, world class waterfront.
Everyone who lives on Puget Sound is convinced they live in the most beautiful and spectacular place in the world, and we're all correct.

Target Market(s)

Members of the Halvern-Ostrow County Bar Association, and more distant counsel seeking consultation re: local conditions.
Also, I decided it was time to have a website, so a reference place to direct clients.
I like the professional sound of .lawyer vs. commercial sound of .com.

Industry/Entity Type

Law Firm

Coding

Coded - Design and coding required

Number of Pages Required

5+ page

Font styles to use
Other font styles liked:
• That newly created "web" font everyone seems to be usIng

Colors
32b8a4
3377b5

Requirements
Must have
• A strong first page with my photo and Puget Sound chart professionally created.
• A page I have ready with local links.
• A "How to find me page", which should have a map, and photo of my office, which I can make with the preloaded templates the host provides.
• A "This is what I do page", with some testimonials, which I can do via said templates or preferably by professionals.
Nice to have
• Clean look.
• Consistent looks to pages.
• First comment I got back talked about just designing one page, and if requires $340.00, so be it.
• Typical local sites have 4/5 pages, so perhaps a "fill-able" generic pages, I can build myself.
• Ideally, I would step into a working site I can edit myself.
• Not looking for e-commerce site, but the remainder of language the "Smart" professional used is unknown to me.
• Bit out of my element here, hoping for guidance.
Should not have
• Clutter

```html
<!DOCTYPE html>
<html lang="en">
<head>
<meta charset="utf-8">
<title>CedarBight.Lawyer</title>
<link href="https://fonts.googleapis.com/css2?family=Questrial&family=Open+Sans:wght@400;600;700&display=swap" rel="stylesheet">
<style>
  :root{
    --blue:#3377b5;
    --blue-deep:#2a6399;
    --teal:#32b8a4;
    --teal-deep:#238a7b;
    --page:#ffffff;
    --soft:#f3f7f8;
    --ink:#1b1f24;
    --body-text:#5a5f66;
    --meta-text:#7a8088;
    --white:#ffffff;
    --rule:#c9d3d8;
  }
  *{box-sizing:border-box;margin:0;padding:0}
  html,body{width:729px;height:1200px;overflow:hidden}
  body{position:relative;background:var(--page);font-family:"Open Sans",Arial,sans-serif;color:var(--ink)}
  .abs{position:absolute}
  .display{font-family:"Questrial","Century Gothic",sans-serif;font-weight:700}

  .top-bar{left:0;top:0;width:729px;height:92px;background:var(--page);border-bottom:1px solid #e4ebee}
  .top-bar .email,.top-bar .phone{top:29px;font-size:8px;color:var(--meta-text)}
  .top-bar .email{left:94px}
  .top-bar .phone{left:500px}
  .brand{left:302px;top:8px;display:flex;align-items:center;gap:7px}
  .brand-dot{width:38px;height:38px;border-radius:50%;background:var(--teal)}
  .brand-name{font-family:"Questrial",sans-serif;font-size:15px;line-height:1.05;color:var(--blue);letter-spacing:.5px}

  .main-nav{left:28px;top:64px;width:671px;height:54px;background:var(--blue);border-radius:3px;z-index:2}
  .main-nav a{position:absolute;top:21px;transform:translateX(-50%);font-size:9.5px;font-weight:700;color:var(--white);text-decoration:none;letter-spacing:.3px;white-space:nowrap}

  .hero{left:0;top:92px;width:729px;height:356px;
    background:linear-gradient(180deg,#3a4350 0%,#8a5a52 18%,#d9725a 33%,#5e4f57 44%,#a15e5a 62%,#6e4a4d 80%,#2b2a2c 100%)}
  .hero-title{left:0;top:219px;width:729px;text-align:center;font-size:34px;line-height:41px;color:var(--white)}
  .hero-sub{left:0;top:312px;width:729px;text-align:center;font-size:14px;color:var(--teal);font-weight:600}
  .btn{display:block;font-size:7px;color:var(--white);text-align:center;line-height:24px;border-radius:3px;text-decoration:none}
  .hero-btn{left:323px;top:353px;width:83px;height:26px;border:1px solid var(--white);background:var(--teal-deep)}
  .slider-arrows{left:348px;top:430px;width:39px;height:18px;background:#d5dde0}

  .welcome{left:0;top:448px;width:729px;height:177px;background:var(--soft)}
  .welcome-title{left:0;top:28px;width:729px;text-align:center;font-size:22px}
  .welcome-title span{color:var(--blue)}
  .welcome .rule{top:41px;height:1px;background:var(--rule);width:152px}
  .welcome p{left:80px;top:70px;width:569px;text-align:center;font-size:7.2px;line-height:13.6px;color:var(--body-text)}
  .welcome-btn{left:324px;top:124px;width:80px;height:25px;background:var(--teal-deep)}

  .section-title{left:0;width:729px;text-align:center}
  .section-title span{color:var(--blue)}
  .services-title{top:646px;font-size:21px}
  .service-tag{height:63px;background:var(--blue);color:var(--white);font-size:13px;display:flex;align-items:center;justify-content:center}
  .service-text{border:1px solid var(--teal);background:var(--white);font-size:8.6px;line-height:15.6px;color:var(--body-text);padding:20px 16px}
  .mini-btn{width:24px;height:22px;background:var(--teal-deep);border-radius:2px}

  .testimonials{left:0;top:956px;width:729px;height:202px;background:var(--blue);color:var(--white)}
  .testimonials h2{left:0;top:30px;width:729px;text-align:center;font-size:20px}
  .quote{left:120px;top:74px;width:489px;text-align:center;font-size:7.5px;line-height:17px}
  .quote-mark{font-family:Georgia,serif;font-size:18px;line-height:0;vertical-align:-4px}
  .client-name{left:0;top:113px;width:729px;text-align:center;font-size:10px}
  .avatar{top:135px;width:51px;height:51px;border-radius:50%;border:2px solid var(--white);background:radial-gradient(circle at 50% 40%,#d3dbe2,#5f7f9c)}
  .avatar.dim{opacity:.55}

  .site-footer{left:0;top:1158px;width:729px;height:42px}
  .site-footer .legal{left:31px;top:18px;font-size:7px;color:var(--ink)}
  .social{top:21px;width:9px;height:9px;border-radius:50%;background:var(--blue)}
</style>
</head>
<body>

<header class="top-bar abs">
  <div class="abs email">Email id : info@cedarbight.lawyer</div>
  <div class="abs brand"><span class="brand-dot"></span><span class="brand-name">CEDARBIGHT<br>LAWYER</span></div>
  <div class="abs phone">Call Us : 123-456-7890</div>
</header>

<nav class="main-nav abs">
  <a style="left:117px">HOME</a>
  <a style="left:209px">ABOUT US</a>
  <a style="left:320px">OUR SERVICES</a>
  <a style="left:427px">CAREERS</a>
  <a style="left:530px">CONTACT US</a>
</nav>

<div class="hero abs" role="img" aria-label="Sunset over calm water with a mountain ridge, a pier and tree silhouettes"></div>
<h1 class="hero-title abs display">Lorem Ipsum Dolor Sit Amet,<br>Consectetur</h1>
<div class="hero-sub abs">Duis aute irure dolor in reprehenderit in voluptate</div>
<a class="btn hero-btn abs">READ MORE</a>
<div class="slider-arrows abs">
  <svg width="39" height="18" viewBox="0 0 39 18"><path d="M15 5l-4 4 4 4M24 5l4 4-4 4" fill="none" stroke="#222" stroke-width="1.4"/></svg>
</div>

<section class="welcome abs">
  <div class="rule abs" style="left:28px"></div>
  <div class="rule abs" style="left:547px"></div>
  <h2 class="welcome-title abs display">Welcome to <span>CEDARBIGHT LAWYER</span></h2>
  <p class="abs">Lorem ipsum dolor sit amet, consectetur adipiscing elit, sed do eiusmod tempor incididunt ut labore et dolore magna aliqua. Ut enim ad minim veniam, quis nostrud exercitation ullamco laboris nisi ut aliquip ex ea commodo consequat. Duis aute irure dolor in reprehenderit in voluptate velit esse cillum dolore eu fugiat nulla pariatur. Excepteur sint occaecat cupidatat non proident, sunt in culpa qui officia deserunt mollit anim id est laborum.</p>
  <a class="btn welcome-btn abs">READ MORE</a>
</section>

<h2 class="section-title services-title abs display">Our <span>Service</span></h2>

<div class="service-tag abs display" style="left:39px;top:705px;width:228px">Lawyer Service</div>
<svg class="abs" style="left:266px;top:721px" width="12" height="18"><path d="M0 0l12 9-12 9z" fill="#3377b5"/></svg>
<div class="service-text abs" style="left:295px;top:703px;width:394px;height:88px">We have many years of experience in all areas of commercial and civil litigation, including tax and licensing disputes. If you are in need of legal representation, our service is always personal and our rates are extremely competitive and flexible.</div>
<div class="mini-btn abs" style="left:649px;top:779px"><svg width="24" height="22"><path d="M10 7l4 4-4 4" fill="none" stroke="#fff" stroke-width="1.5"/></svg></div>

<div class="service-text abs" style="left:40px;top:822px;width:395px;height:88px;text-align:right">Our notary services are committed to providing the fastest and easiest way to ensure timely and accurate document signings. We are here to provide loan document signing services to lenders, brokers, escrow, title, and legal companies</div>
<div class="service-tag abs display" style="left:465px;top:823px;width:234px">Notary Services</div>
<svg class="abs" style="left:454px;top:838px" width="12" height="18"><path d="M12 0L0 9l12 9z" fill="#3377b5"/></svg>
<div class="mini-btn abs" style="left:63px;top:899px"><svg width="24" height="22"><path d="M14 7l-4 4 4 4" fill="none" stroke="#fff" stroke-width="1.5"/></svg></div>

<section class="testimonials abs">
  <h2 class="abs display">Client Testimonials</h2>
  <p class="quote abs"><span class="quote-mark">“</span> Lorem ipsum dolor sit amet, consectetur adipiscing elit, sed do eiusmod tempor incididunt ut labore et dolore magna aliqua.<br>Ut enim ad minim veniam, quis nostrud exercitation ullamco laboris.<span class="quote-mark">”</span></p>
  <div class="client-name abs">- DANA WHITLOCK</div>
  <div class="avatar abs" style="left:286px" role="img" aria-label="Client portrait"></div>
  <div class="avatar dim abs" style="left:346px" role="img" aria-label="Client portrait"></div>
  <div class="avatar abs" style="left:406px" role="img" aria-label="Client portrait"></div>
</section>

<footer class="site-footer abs">
  <div class="legal abs">All Rights Reserved. Copyrights @company Name. 2016</div>
  <span class="social abs" style="left:596px"></span>
  <span class="social abs" style="left:620px"></span>
  <span class="social abs" style="left:643px"></span>
  <span class="social abs" style="left:665px"></span>
  <span class="social abs" style="left:689px"></span>
</footer>

</body>
</html>
```